PowerPoint Design Project

Design Brief
Corvanta is updating its stationary templates to reflect the company’s position as market leader in smart-location based solutions.
Using the existing Corvanta logo and corporate colours, create an engaging and visually appealing PowerPoint presentation template identity that works when printed on A4 and US Letter sized paper.
The successful designs will complement the current look and feel of the Corvanta website (www.corvanta-example.net) and communicate that Corvanta is a dynamic and modern technology company that is at the cutting edge of innovation.
Corvanta Brand
Corvanta stands for Precision Location Technology. The brand represents both a unique, highly innovative platform product and a mature consulting and support organisation dedicated to delivering solutions to blue-chip customer problems. The orange colour implies creativity while blue evokes trust and a rational approach. “Cor” is Latin and means “where”, so the brand directly addresses the focus of the company: location. “Sense” can mean that we have sensing technology to support our precision location aware applications and solutions, but also that we make sensible use of location data to improve customer processes.
Corvanta Corporate Profile
Corvanta is a market leader of location-based Smart Factory Solutions which enables companies to optimise their business processes. By keeping track of key assets, Corvanta solutions bring clarity to complex operations in industries while also improving quality and reliability. Corvanta uses a unique combination of advancefd industry knowledge and an experienced team to deliver effective and superior solutions that offer unprecedented visibility, control and accuracy, delivering time and cost savings. Corvanta solutions are easy to implement and flexible to a particular business’s needs, no matter which area of the globe they operate in.
Corvanta offers two location-oriented products; RTLS (Real-time Location Solutions) and Geospatial Systems and operates in a number of industries ranging from manufacturing and utilities to telecommunications and is used by a number of blue chip customers across the world, such as KLT, Skyvane, Dromtrack, Pellow Power, RIM and Nordfeld Fernmelde.
Corvanta Corporate Colours
Orange:
Pantone 021C
R: 237 / G: 110 / B: 0
C: 0 / M: 53 / Y: 100 / K: 0
Hex #ED6E00
Dark Blue:
Pantone 662C
R: 15 / G: 31 / B: 122
C: 100 / M: 71 / Y: 0 / K:0
Hex #0F1F7A
Light Blue:
Pantone 300C
R: 0 / G: 110 / B: 199
C: 100 / M: 44 / Y: 0 / K:0
Hex #006EC7
Corvanta Corporate Fonts
The preferred font is Tahoma for Title, Topics and Print. In certain situations, Arial is an acceptable alternative.
Target Market(s)
Manufacturing industry, Automotive and Aerospace
Industry/Entity Type
Telecommunications
Look and feel
Each slider illustrates characteristics of the customer's brand and the style your logo design should communicate.

```html
<!DOCTYPE html>
<html lang="en">
<head>
<meta charset="utf-8">
<title>Corvanta Presentation Template</title>
<link rel="stylesheet" href="https://fonts.googleapis.com/css2?family=PT+Sans:wght@400;700&family=Noto+Serif&display=swap">
<style>
  :root {
    --stage: #808080;
    --orange: #f7941d;
    --orange-line: #ed6e00;
    --brand-blue: #006ec7;
    --band-dark: #454a50;
    --band-light: #c8cacc;
    --paper: #ffffff;
    --slide-grey: #efefef;
    --ink: #1a1a1a;
    --photo-factory: #7a5a44;
  }
  * { margin: 0; padding: 0; box-sizing: border-box; }
  html, body { width: 1200px; height: 900px; overflow: hidden; }
  body {
    background: var(--stage);
    font-family: "PT Sans", Arial, sans-serif;
    position: relative;
  }
  .slide { position: absolute; overflow: hidden; background: var(--paper); }

  .brand { display: flex; align-items: center; gap: 8px; color: var(--brand-blue); font-weight: 400; }
  .brand-mark { border-radius: 50%; background: var(--orange-line); }

  /* Title slide */
  .slide-title { left: 34px; top: 24px; width: 542px; height: 416px; }
  .slide-title .brand { position: absolute; left: 36px; top: 48px; font-size: 29px; }
  .slide-title .brand-mark { width: 26px; height: 26px; }
  .slide-title .rule { position: absolute; left: 0; top: 148px; width: 100%; height: 3px; background: var(--orange-line); }
  .slide-title .hero { position: absolute; left: 0; top: 154px; width: 100%; height: 140px;
    background: linear-gradient(100deg, #5a5048 0%, var(--photo-factory) 30%, #b39a7c 55%, #6b5a4a 80%, #8a3a20 100%); }
  .band { position: absolute; left: 0; width: 100%; height: 12px; display: flex; }
  .band .dark { background: var(--band-dark); height: 100%; }
  .band .light { background: var(--band-light); height: 100%; flex: 1; }
  .slide-title .band { top: 294px; }
  .slide-title .band .dark { width: 380px; }
  .slide-title .cover { position: absolute; left: 0; top: 306px; width: 100%; height: 110px;
    background: var(--orange); display: flex; align-items: center; justify-content: center;
    text-align: center; font-size: 24px; line-height: 1.25; color: var(--ink); }

  /* Content slide */
  .slide-content { left: 612px; top: 24px; width: 544px; height: 416px; background: var(--slide-grey); }
  .slide-content .heading { position: absolute; left: 14px; top: 14px; display: flex; align-items: center; width: 530px; }
  .slide-content .heading h1 { font-size: 30px; font-weight: 400; color: #000; white-space: nowrap; margin-right: 6px; }
  .slide-content .heading .line { flex: 1; height: 2px; background: var(--orange-line); }
  .slide-content .band { top: 362px; }
  .slide-content .band .dark { width: 380px; }
  .slide-content .band .light { position: relative; }
  .page-number { position: absolute; right: 22px; top: 1px; width: 20px; height: 10px; border-radius: 50%;
    background: #111; color: #fff; font-size: 9px; line-height: 10px; text-align: center; }
  .slide-content .footer { position: absolute; left: 0; top: 374px; width: 100%; height: 42px;
    background: var(--paper); border-top: 3px solid var(--orange-line);
    display: flex; align-items: center; justify-content: space-between; padding: 0 22px 0 20px; }
  .slide-content .footer .brand { font-size: 17px; gap: 5px; }
  .slide-content .footer .brand-mark { width: 15px; height: 15px; }
  .legal { font-size: 9px; color: var(--ink); white-space: nowrap; }

  /* Closing slide */
  .slide-closing { left: 340px; top: 460px; width: 540px; height: 420px; }
  .slide-closing .stage-orange { position: absolute; left: 0; top: 0; width: 100%; height: 270px; background: var(--orange); }
  .slide-closing .gallery { position: absolute; left: 42px; top: 34px; width: 216px; height: 202px;
    border: 2px solid var(--paper); border-radius: 6px;
    background: linear-gradient(135deg, #8a8a84 0%, #3b6fb5 35%, #7d7f84 65%, #6f8a3c 100%); }
  .slide-closing .thanks { position: absolute; left: 280px; top: 134px; font-family: "Noto Serif", Georgia, serif;
    font-size: 19px; color: #fff; white-space: nowrap; }
  .slide-closing .band { top: 270px; }
  .slide-closing .band .dark { width: 382px; }
  .slide-closing .brand { position: absolute; left: 50%; top: 318px; transform: translateX(-50%); font-size: 29px; }
  .slide-closing .brand-mark { width: 26px; height: 26px; }
  .slide-closing .closing-legal { position: absolute; left: 32px; right: 22px; top: 384px;
    display: flex; justify-content: space-between; }
</style>
</head>
<body>

<section class="slide slide-title">
  <div class="brand"><span class="brand-mark"></span><span>Corvanta</span></div>
  <div class="rule"></div>
  <div class="hero" role="img" aria-label="Photo of robotic welding arms on a car body assembly line"></div>
  <div class="band"><span class="dark"></span><span class="light"></span></div>
  <div class="cover"><p>Powerpoint Presentation<br>Title Here</p></div>
</section>

<section class="slide slide-content">
  <div class="heading"><h1>Heading 1</h1><span class="line"></span></div>
  <div class="band"><span class="dark"></span><span class="light"><span class="page-number">2</span></span></div>
  <footer class="footer">
    <div class="brand"><span class="brand-mark"></span><span>Corvanta</span></div>
    <span class="legal">© 2012 Corvanta Confidential &amp; Proprietary</span>
  </footer>
</section>

<section class="slide slide-closing">
  <div class="stage-orange"></div>
  <div class="gallery" role="img" aria-label="Collage of industry photos: a vehicle on a production line, a blue locomotive, green machinery and a rail carriage"></div>
  <p class="thanks">Thank you for watching!</p>
  <div class="band"><span class="dark"></span><span class="light"></span></div>
  <div class="brand"><span class="brand-mark"></span><span>Corvanta</span></div>
  <div class="closing-legal">
    <span class="legal">© 2012 Corvanta Confidential &amp; Proprietary</span>
    <span class="legal">www.corvanta-example.net</span>
  </div>
</section>

</body>
</html>
```